Quarvella Brochure Design - IT Services - Modern Design - Services List

Hi,

We are looking for a modern IT Services brochure design of between 4 - 6 pages, it must be based on a blue and white colour theme with some nice technical imagery. It would need a section about why Quarvella and a contact section at the end.

Here is some info that could be included

Target Market(s)

Medium to Large Businesses

Industry/Entity Type

Information Technology

Colors
0054AA
0677BA
7BADD7
CADEEF
E8F1F8

Requirements
Must have
• Striking technical imagery
Nice to have
• Nice Icons to list the different services sections

```html
<!DOCTYPE html>
<html lang="en">
<head>
<meta charset="utf-8">
<title>Quarvella IT Services Brochure</title>
<link rel="stylesheet" href="https://fonts.googleapis.com/css2?family=Montserrat:wght@400;500;600;700&family=Open+Sans:wght@400;600;700&display=swap">
<style>
:root{
  --canvas:#6f6f6f;
  --blue:#3b7cc8;
  --deep:#0054AA;
  --azure:#0677BA;
  --cyan:#1c9de2;
  --sky:#7BADD7;
  --pale:#CADEEF;
  --mist:#E8F1F8;
  --ink:#1d1d1d;
  --grey:#5c5c5c;
  --band:#c6c7c9;
  --soft:#f3f3f3;
  --paper:#ffffff;
}
*{box-sizing:border-box;margin:0;padding:0}
html,body{width:1200px;height:3599px;overflow:hidden;background:var(--canvas)}
.sheet{position:absolute;left:0;top:0;width:859px;height:2576px;transform:scale(1.39697);transform-origin:0 0;font-family:"Open Sans",Arial,sans-serif;color:var(--grey)}
.page{position:absolute;width:344px;height:488px;overflow:hidden;background:var(--paper)}
.abs{position:absolute}
.head{font-family:"Montserrat",Arial,sans-serif;font-weight:600;color:var(--ink);letter-spacing:.2px;line-height:1.25}
.head .hl{color:var(--cyan)}
.body{font-size:3.9px;line-height:1.85;text-align:justify}
.tiny{font-size:3.2px;line-height:1.6}
.photo{position:absolute}

/* cover */
.cover-brand{font-family:"Montserrat",Arial,sans-serif;font-weight:700;font-size:24px;color:var(--azure);letter-spacing:.5px}
.cover-tag{font-family:"Montserrat",Arial,sans-serif;font-weight:600;font-size:5.6px;color:var(--ink)}
.cover-title{font-size:27px;font-weight:700;line-height:1.15}
.contact-head{font-family:"Montserrat",Arial,sans-serif;font-weight:600;font-size:6px;color:#777}
.contact-head.caps{font-size:5px}

/* checklist */
.check{position:absolute;display:flex;align-items:flex-start;gap:6px;font-size:6px;line-height:1.3;color:var(--grey)}
.check svg{flex:none}

/* footers */
.folio{position:absolute;top:450px;font-size:5px;font-weight:700;color:var(--ink)}
.rule{position:absolute;top:454px;height:1px;background:var(--sky)}
.rule .run{position:absolute;left:0;top:-.5px;height:2px;background:var(--cyan)}
.foot-note{position:absolute;top:448px;font-size:2.8px;line-height:1.5;width:40px}

/* stats */
.stat{position:absolute;top:362px;color:#fff;width:78px}
.stat .num{font-family:"Montserrat",Arial,sans-serif;font-weight:700;font-size:19px;letter-spacing:.3px}
.stat .lab{font-family:"Montserrat",Arial,sans-serif;font-size:8.4px;line-height:1.25;margin-top:4px;color:#e9f1fa}

/* services */
.svc{position:absolute;top:210px;width:100px;color:#fff}
.svc-icon{position:absolute;top:-3px;width:48px;height:48px;border-radius:50%;background:#fff;display:flex;align-items:center;justify-content:center}
.svc-title{position:absolute;top:61px;font-family:"Montserrat",Arial,sans-serif;font-weight:600;font-size:6.6px;white-space:nowrap}
.svc-text{position:absolute;top:74px;width:100px;font-size:3.6px;line-height:2;color:#eef4fb}
.svc-text p{text-align:justify}
.svc-text ul{list-style:none;margin-top:1px}
.svc-text li{padding-left:4px;text-indent:-3px}

/* cyber band */
.threat{position:absolute;top:12px;width:60px;color:#fff}
.threat svg{display:block;margin:0 auto 9px 14px}
.threat p{font-family:"Montserrat",Arial,sans-serif;font-weight:700;font-size:3.4px;line-height:1.8}

/* consulting grid */
.consult{position:absolute;width:130px;text-align:center}
.consult .dot{width:30px;height:30px;border-radius:50%;background:var(--cyan);margin:0 auto;display:flex;align-items:center;justify-content:center}
.consult h4{font-family:"Montserrat",Arial,sans-serif;font-weight:600;font-size:4.6px;line-height:1.7;color:var(--ink);margin-top:9px}
.consult p{font-size:3.7px;line-height:1.9;margin-top:6px}

/* why */
.why-sub{position:absolute;left:26px;font-family:"Montserrat",Arial,sans-serif;font-weight:500;font-size:8.6px;color:var(--sky)}
.why-text{position:absolute;left:26px;width:180px;font-size:3.7px;line-height:1.85;color:#444}
</style>
</head>
<body>
<main class="sheet">

<!-- Front cover -->
<section class="page cover" style="left:89px;top:56px">
  <svg class="abs" width="344" height="488" viewBox="0 0 344 488" style="left:0;top:0">
    <defs>
      <clipPath id="lens"><circle cx="150" cy="60" r="165"/></clipPath>
      <linearGradient id="lensFill" x1="0" y1="0" x2="1" y2="1">
        <stop offset="0" stop-color="#0b2a44"/>
        <stop offset=".45" stop-color="#0f4f77"/>
        <stop offset=".7" stop-color="#12324f"/>
        <stop offset="1" stop-color="#061420"/>
      </linearGradient>
    </defs>
    <path d="M0,196 C70,262 160,282 262,266 C180,292 80,340 0,414 Z" fill="var(--cyan)"/>
    <circle cx="150" cy="60" r="171" fill="none" stroke="#8d8d8d" stroke-width="9"/>
    <g role="img" aria-label="Photo of a woman working at a laptop surrounded by glowing code screens">
      <rect x="0" y="0" width="344" height="240" fill="url(#lensFill)" clip-path="url(#lens)"/>
    </g>
    <path d="M249,-93 A182,182 0 0 1 299,164" fill="none" stroke="var(--cyan)" stroke-width="3"/>
  </svg>

  <div class="abs cover-brand" style="right:55px;top:281px">Quarvella</div>
  <div class="abs cover-tag" style="right:55px;top:320px">COMPUTING EXCELLENCE</div>
  <h1 class="abs head cover-title" style="left:88px;top:342px"><span class="hl">QUARVELLA</span> IT<br>SERVICES</h1>

  <div class="abs" style="left:35px;top:418px;width:230px;height:1px;background:var(--sky)"></div>
  <div class="abs" style="left:35px;top:424px;width:80px">
    <div class="contact-head">Contact Us</div>
    <div class="tiny">Website: www.quarvella.co.uk<br>Email: hello@quarvella.co.uk<br>Phone: 0161 555 0192<br>Email: info@quarvella.co.uk</div>
  </div>
  <div class="abs" style="left:118px;top:425px;width:55px">
    <div class="contact-head caps">ADDRESS TO</div>
    <div class="tiny">48 Harbour Lane,<br>Tech Park, Leeds,<br>UK</div>
  </div>
  <div class="abs" style="left:177px;top:424px;width:65px">
    <div class="contact-head">Follow Us</div>
    <div class="tiny">Stay updated with the latest<br>news and updates from Quarvella.</div>
  </div>
  <div class="abs tiny" style="left:245px;top:432px">Profile (QRV)<br>Feed (QRV)<br>Page (QRV)</div>
</section>

<!-- Page 2: About -->
<section class="page" style="left:89px;top:555px;background:var(--soft)">
  <div class="abs" style="left:236px;top:0;width:108px;height:488px;background:var(--blue)"></div>
  <div class="photo" role="img" aria-label="Photo of a technician working at a computer in a server room" style="left:236px;top:67px;width:108px;height:280px;background:linear-gradient(160deg,#d9dde2,#9aa7b4 55%,#5b6774)"></div>

  <h2 class="abs head" style="left:36px;top:63px;font-size:14px">ABOUT <span class="hl">QUARVELLA</span></h2>
  <p class="abs body" style="left:36px;top:91px;width:180px">At Quarvella, we are dedicated to providing top-tier IT services that drive efficiency, innovation, and growth for your business. With a commitment to excellence and a team of highly skilled professionals, we offer a comprehensive suite of solutions tailored to meet the unique needs of our clients.</p>
  <h3 class="abs head" style="left:36px;top:138px;font-size:8.6px;font-weight:500;color:var(--grey);line-height:1.35">GROW YOUR BUSINESS SAFELY<br>AND SECURELY WITH OUR<br>MANAGED IT SERVICES</h3>
  <p class="abs body" style="left:36px;top:179px;width:180px;text-align:left">Managed IT Services delivered professionally, on-time,<br>and guaranteed to EXCEED expectations.</p>

  <div class="check" style="left:32px;top:208px"><svg width="12" height="12" viewBox="0 0 12 12"><circle cx="6" cy="6" r="6" fill="var(--azure)"/><path d="M3.2 6.2 5.1 8 8.9 4.1" fill="none" stroke="#fff" stroke-width="1.3"/></svg><span>Hardware<br>Monitoring</span></div>
  <div class="check" style="left:129px;top:208px"><svg width="12" height="12" viewBox="0 0 12 12"><circle cx="6" cy="6" r="6" fill="var(--azure)"/><path d="M3.2 6.2 5.1 8 8.9 4.1" fill="none" stroke="#fff" stroke-width="1.3"/></svg><span>Security Patching and<br>Protection</span></div>
  <div class="check" style="left:32px;top:238px"><svg width="12" height="12" viewBox="0 0 12 12"><circle cx="6" cy="6" r="6" fill="var(--azure)"/><path d="M3.2 6.2 5.1 8 8.9 4.1" fill="none" stroke="#fff" stroke-width="1.3"/></svg><span>Disaster<br>Recovery Solutions</span></div>
  <div class="check" style="left:129px;top:240px"><svg width="12" height="12" viewBox="0 0 12 12"><circle cx="6" cy="6" r="6" fill="var(--azure)"/><path d="M3.2 6.2 5.1 8 8.9 4.1" fill="none" stroke="#fff" stroke-width="1.3"/></svg><span style="padding-top:3px">Resource Monitoring</span></div>

  <h2 class="abs head" style="left:36px;top:290px;font-size:14px;line-height:1.45">TECHNOLOGY<br>SOLUTIONS <span class="hl">FOR<br>YOUR BUSINESS</span></h2>

  <div class="check" style="left:32px;top:360px"><svg width="12" height="12" viewBox="0 0 12 12"><circle cx="6" cy="6" r="6" fill="var(--azure)"/><path d="M3.2 6.2 5.1 8 8.9 4.1" fill="none" stroke="#fff" stroke-width="1.3"/></svg><span>Business Broadband<br>Solutions</span></div>
  <div class="check" style="left:129px;top:360px"><svg width="12" height="12" viewBox="0 0 12 12"><circle cx="6" cy="6" r="6" fill="var(--azure)"/><path d="M3.2 6.2 5.1 8 8.9 4.1" fill="none" stroke="#fff" stroke-width="1.3"/></svg><span>Managed<br>Print Services</span></div>
  <div class="check" style="left:32px;top:393px"><svg width="12" height="12" viewBox="0 0 12 12"><circle cx="6" cy="6" r="6" fill="var(--azure)"/><path d="M3.2 6.2 5.1 8 8.9 4.1" fill="none" stroke="#fff" stroke-width="1.3"/></svg><span style="padding-top:3px">Cloud Backups</span></div>
  <div class="check" style="left:129px;top:393px"><svg width="12" height="12" viewBox="0 0 12 12"><circle cx="6" cy="6" r="6" fill="var(--azure)"/><path d="M3.2 6.2 5.1 8 8.9 4.1" fill="none" stroke="#fff" stroke-width="1.3"/></svg><span style="padding-top:3px">VoIP Telephony</span></div>

  <div class="folio" style="left:36px">2</div>
  <div class="rule" style="left:52px;width:176px"><span class="run" style="width:60px"></span></div>
  <div class="foot-note" style="left:262px;color:#e6eef8">Summary of the company during the past years</div>
</section>

<!-- Page 3: Stats -->
<section class="page" style="left:438px;top:555px;background:var(--blue)">
  <div class="photo" role="img" aria-label="Photo of two engineers checking a server rack in a data centre" style="left:0;top:67px;width:310px;height:278px;background:linear-gradient(110deg,#b9c1ca,#e6e9ec 35%,#6c7782 65%,#1f262e)"></div>
  <div class="abs" style="left:165px;top:102px;width:115px;height:151px;background:#fff;padding:10px 12px 0 14px">
    <svg width="26" height="20" viewBox="0 0 26 20"><path d="M0 11c0-6 4-11 10-11v4c-3 0-5 2-5 5h5v11H0zM14 11c0-6 4-11 10-11v4c-3 0-5 2-5 5h5v11H14z" fill="var(--azure)"/></svg>
    <p style="margin-top:8px;font-size:6.6px;line-height:1.95;color:var(--ink)">Sometimes when things go wrong with your IT and you need assistance, but when they go REALLY wrong you need help QUICKLY!</p>
    <p class="tiny" style="margin-top:3px;color:#333">With our ad-hoc IT Support you can just call us up and we can help you fix the problem at an affordable hourly rate fast.</p>
  </div>

  <div class="stat" style="left:12px"><div class="num">300 +</div><div class="lab">MIGRATIONS<br>TO THE<br>CLOUD</div></div>
  <div class="stat" style="left:90px"><div class="num">400 +</div><div class="lab">POSITIVE<br>FEEDBACK<br>RECEIVED</div></div>
  <div class="stat" style="left:168px"><div class="num">300 +</div><div class="lab">CLOUD SUITE<br>MIGRATIONS</div></div>
  <div class="stat" style="left:246px"><div class="num">3000 +</div><div class="lab">MAILBOXES<br>SUPPORTED</div></div>

  <div class="foot-note" style="left:36px;color:#e6eef8">Quarvella IT Services Brochure</div>
  <div class="rule" style="left:88px;width:205px;background:var(--pale)"></div>
  <div class="folio" style="left:303px;color:#fff">3</div>
</section>

<!-- Page 4: Services -->
<section class="page" style="left:89px;top:1048px;background:var(--blue)">
  <div class="abs" style="left:0;top:0;width:344px;height:107px;background:#fff"></div>
  <div class="photo" role="img" aria-label="Photo of a softly lit server room corridor" style="left:131px;top:0;width:213px;height:107px;background:linear-gradient(90deg,#ffffff,#e3e6e9 30%,#b8bec5 65%,#8c96a0)"></div>
  <h2 class="abs head" style="left:36px;top:64px;font-size:14px">OUR <span class="hl">SERVICES</span></h2>
  <div class="abs" style="left:0;top:107px;width:344px;height:68px;background:var(--band)"></div>
  <div class="abs" style="left:36px;top:120px;font-family:'Montserrat',Arial,sans-serif;font-weight:600;font-size:4.6px;line-height:2;color:#fff">AWARD-WINNING<br>MANAGED IT SERVICES</div>
  <p class="abs tiny" style="left:172px;top:116px;width:108px;color:#fff">Professional IT Services from a team that cares. We have over 25 years of experience supporting businesses small, medium, and large, deploying comprehensive technology solutions that have helped them become secure and grow.</p>

  <div class="svc" style="left:60px">
    <div class="svc-icon" style="left:18px"><svg width="26" height="26" viewBox="0 0 26 26" fill="none" stroke="var(--azure)" stroke-width="1.6"><rect x="5" y="13" width="16" height="9" rx="1"/><path d="M3 23h20M13 3v10M6 8h14M6 8v5M20 8v5"/><circle cx="13" cy="3" r="2"/></svg></div>
    <div class="svc-title" style="left:0">MANAGED IT SERVICES</div>
    <div class="svc-text" style="left:0">
      <p>Our Managed IT Services provide proactive monitoring and management of your IT infrastructure, ensuring maximum uptime and reliability. We offer:</p>
      <ul>
        <li>• 24/7 Network Monitoring: Continuous monitoring to detect and resolve issues before they impact your business.</li>
        <li>• Helpdesk Support: Responsive and knowledgeable support team available round the clock.</li>
        <li>• Patch Management: Regular updates and patches to keep your systems secure and up-to-date.</li>
        <li>• IT Asset Management: Comprehensive tracking and management of your IT assets.</li>
      </ul>
    </div>
  </div>
  <div class="svc" style="left:197px">
    <div class="svc-icon" style="left:14px"><svg width="26" height="26" viewBox="0 0 26 26"><path d="M7 15a5 5 0 0 1 1-10 6 6 0 0 1 11 2 4 4 0 0 1 0 8z" fill="var(--azure)"/><path d="M13 15v7M8 15v4M18 15v4" stroke="var(--azure)" stroke-width="1.5"/><circle cx="13" cy="23" r="1.6" fill="var(--azure)"/><circle cx="8" cy="20" r="1.6" fill="var(--azure)"/><circle cx="18" cy="20" r="1.6" fill="var(--azure)"/></svg></div>
    <div class="svc-title" style="left:0">CLOUD SOLUTIONS</div>
    <div class="svc-text" style="left:0">
      <p>Embrace the power of the cloud with our scalable and secure cloud solutions. Our offerings include:</p>
      <ul>
        <li>• Cloud Migration: Seamless transition of your applications and data to the cloud.</li>
        <li>• Cloud Hosting: Reliable and scalable hosting solutions to meet your growing needs.</li>
        <li>• Backup and Disaster Recovery: Robust backup and recovery solutions to ensure business continuity.</li>
        <li>• Software as a Service (SaaS): Access to the latest software applications without the hassle of maintenance.</li>
      </ul>
    </div>
  </div>

  <div class="folio" style="left:36px;color:#fff">4</div>
  <div class="rule" style="left:52px;width:200px;background:var(--pale)"><span class="run" style="width:60px;background:var(--sky)"></span></div>
  <div class="foot-note" style="left:262px;color:#e6eef8">Quarvella IT Services Brochure</div>
</section>

<!-- Page 5: Services continued -->
<section class="page" style="left:438px;top:1048px;background:#fff">
  <div class="photo" role="img" aria-label="Close-up photo of hands typing on a keyboard" style="left:0;top:0;width:344px;height:107px;background:linear-gradient(100deg,#aab2bb,#d3cfcb 40%,#9b8f88 70%,#6f6863)"></div>
  <div class="photo" role="img" aria-label="Continuation of the keyboard photo" style="left:273px;top:107px;width:71px;height:103px;background:linear-gradient(180deg,#6f6863,#4d4f55)"></div>
  <div class="abs" style="left:0;top:107px;width:273px;height:68px;background:var(--band)"></div>
  <p class="abs tiny" style="left:36px;top:119px;width:90px;color:#fff">At Quarvella, we pride ourselves on being more than a technology partner, we're a trusted extension of your team.</p>
  <div class="abs" style="left:0;top:175px;width:273px;height:313px;background:var(--blue)"></div>

  <div class="svc" style="left:20px">
    <div class="svc-icon" style="left:16px"><svg width="26" height="26" viewBox="0 0 26 26"><path d="M13 2 22 6v7c0 5-4 9-9 11-5-2-9-6-9-11V6z" fill="none" stroke="var(--azure)" stroke-width="1.6"/><rect x="9" y="12" width="8" height="6" rx="1" fill="var(--azure)"/><path d="M10.5 12V10a2.5 2.5 0 0 1 5 0v2" fill="none" stroke="var(--azure)" stroke-width="1.4"/></svg></div>
    <div class="svc-title" style="left:0">CYBERSECURITY</div>
    <div class="svc-text" style="left:0">
      <p>Our Managed IT Services provide proactive monitoring and management of your IT infrastructure, ensuring maximum uptime and reliability. We offer:</p>
      <ul>
        <li>• 24/7 Network Monitoring: Continuous monitoring to detect and resolve issues before they impact your business.</li>
        <li>• Helpdesk Support: Responsive and knowledgeable support team available round the clock.</li>
        <li>• Patch Management: Regular updates and patches to keep your systems secure and up-to-date.</li>
        <li>• IT Asset Management: Comprehensive tracking and management of your IT assets.</li>
      </ul>
    </div>
  </div>
  <div class="svc" style="left:137px">
    <div class="svc-icon" style="left:12px"><svg width="26" height="26" viewBox="0 0 26 26"><circle cx="13" cy="13" r="10" fill="none" stroke="var(--azure)" stroke-width="3" stroke-dasharray="4 2.3"/><circle cx="13" cy="13" r="6.5" fill="var(--azure)"/><path d="M11 10.5 8.8 13l2.2 2.5M15 10.5l2.2 2.5-2.2 2.5" fill="none" stroke="#fff" stroke-width="1.1"/></svg></div>
    <div class="svc-title" style="left:0">IT CONSULTING</div>
    <div class="svc-text" style="left:0">
      <p>Our Managed IT Services provide proactive monitoring and management of your IT infrastructure, ensuring maximum uptime and reliability. We offer:</p>
      <ul>
        <li>• 24/7 Network Monitoring: Continuous monitoring to detect and resolve issues before they impact your business.</li>
        <li>• Helpdesk Support: Responsive and knowledgeable support team available round the clock.</li>
        <li>• Patch Management: Regular updates and patches to keep your systems secure and up-to-date.</li>
        <li>• IT Asset Management: Comprehensive tracking and management of your IT assets.</li>
      </ul>
    </div>
  </div>

  <div class="foot-note" style="left:36px;color:#e6eef8">Quarvella IT Services Brochure</div>
  <div class="rule" style="left:88px;width:205px;background:var(--pale)"><span class="run" style="left:145px;width:60px"></span></div>
  <div class="folio" style="left:303px">5</div>
</section>

<!-- Page 6: Cybersecurity & Consulting -->
<section class="page" style="left:89px;top:1542px">
  <h2 class="abs head" style="left:36px;top:34px;font-size:14px;color:var(--cyan)">CYBERSECURITY</h2>
  <p class="abs" style="left:36px;top:53px;width:230px;font-size:5.6px;line-height:1.75;color:#444">Protect your business from evolving threats with our comprehensive cybersecurity services. We offer:</p>

  <div class="abs" style="left:36px;top:88px;width:308px;height:88px;background:var(--blue)">
    <div class="threat" style="left:16px"><svg width="12" height="14" viewBox="0 0 12 14" fill="none" stroke="#fff" stroke-width="1"><path d="M3 9a4.5 4.5 0 1 1 6 0c-.8.7-1 1.5-1 2H4c0-.5-.2-1.3-1-2zM4.5 12.5h3"/></svg><p>THREAT DETECTION AND RESPONSE: ADVANCED THREAT MONITORING AND RESPONSE TO SAFEGUARD YOUR DATA.</p></div>
    <div class="threat" style="left:86px"><svg width="14" height="14" viewBox="0 0 14 14" fill="none" stroke="#fff" stroke-width="1"><path d="M4 1h6v4a3 3 0 0 1-6 0zM4 2H1.5a2.5 2.5 0 0 0 2.6 3M10 2h2.5a2.5 2.5 0 0 1-2.6 3M7 8v3M4.5 13h5"/></svg><p>SECURITY AUDITS AND ASSESSMENTS: THOROUGH EVALUATIONS TO IDENTIFY AND MITIGATE VULNERABILITIES.</p></div>
    <div class="threat" style="left:154px"><svg width="14" height="14" viewBox="0 0 14 14" fill="none" stroke="#fff" stroke-width="1"><path d="M2 8V7a5 5 0 0 1 10 0v1M1.5 8h2.5v4H1.5zM10 8h2.5v4H10z"/></svg><p>ENDPOINT PROTECTION: ROBUST SECURITY SOLUTIONS FOR ALL YOUR DEVICES.</p></div>
    <div class="threat" style="left:224px"><svg width="14" height="14" viewBox="0 0 14 14" fill="none" stroke="#fff" stroke-width="1"><circle cx="7" cy="7" r="2.2"/><path d="M7 1v2M7 11v2M1 7h2M11 7h2M2.8 2.8l1.4 1.4M9.8 9.8l1.4 1.4M2.8 11.2l1.4-1.4M9.8 4.2l1.4-1.4"/></svg><p>COMPLIANCE AND REGULATORY SERVICES: ENSURE ADHERENCE TO INDUSTRY STANDARDS AND REGULATIONS.</p></div>
  </div>

  <h2 class="abs head" style="left:36px;top:188px;font-size:14px">IT <span class="hl">CONSULTING</span></h2>
  <p class="abs" style="left:36px;top:206px;width:250px;font-size:5.6px;line-height:1.75;color:#444">Leverage our expertise to drive your IT strategy and achieve your business goals. Our consulting services include:</p>

  <div class="abs" style="left:172px;top:235px;width:1px;height:190px;background:#e4e4e4"></div>
  <div class="abs" style="left:40px;top:333px;width:260px;height:1px;background:#f0f0f0"></div>

  <div class="consult" style="left:40px;top:237px"><div class="dot"><svg width="14" height="14" viewBox="0 0 14 14" fill="none" stroke="#fff" stroke-width="1.2"><path d="M3 13V1.5h7.5l-1.5 2.5 1.5 2.5H3"/></svg></div><h4>IT STRATEGY AND<br>PLANNING</h4><p>Strategic guidance to align your IT initiatives with<br>your business objectives.</p></div>
  <div class="consult" style="left:175px;top:237px"><div class="dot"><svg width="14" height="14" viewBox="0 0 14 14" fill="none" stroke="#fff" stroke-width="1.1"><path d="M3 2h8l2.5 3.5L7 13 .5 5.5zM.5 5.5h13M5 2 4 5.5 7 13l3-7.5L9 2"/></svg></div><h4>TECHNOLOGY<br>ASSESSMENTS</h4><p>In-depth evaluations to optimize your IT infrastructure.</p></div>
  <div class="consult" style="left:40px;top:342px"><div class="dot"><svg width="14" height="14" viewBox="0 0 14 14" fill="none" stroke="#fff" stroke-width="1.1"><path d="M4.5 1.5h5L8 4.5c3 1.5 4 4 3.5 6S9 13 7 13s-4-1-4.5-2.5S3 6 6 4.5z"/><path d="M7 6.5v5M8.2 7.5c-.4-.5-2.4-.5-2.4.6 0 1.2 2.4.6 2.4 1.8 0 1-2 1-2.5.4"/></svg></div><h4>PROJECT MANAGEMENT</h4><p>Lorem Ipsum is simply dummy text of the printing and typesetting industry. Lorem Ipsum has been the industry's standard dummy text ever since the 1500s. The standard chunk of Lorem.</p></div>
  <div class="consult" style="left:175px;top:342px"><div class="dot"><svg width="14" height="14" viewBox="0 0 14 14" fill="none" stroke="#fff" stroke-width="1.1"><path d="M1.5 1.5h11v8H5L2 12.5V9.5H1.5zM4 4.5h6M4 7h4"/></svg></div><h4>BUSINESS CONTINUITY PLANNING</h4><p>Strategies to ensure your business remains<br>operational during disruptions.</p></div>

  <div class="folio" style="left:36px">6</div>
  <div class="rule" style="left:52px;width:200px"><span class="run" style="width:60px"></span></div>
  <div class="foot-note" style="left:262px">Quarvella IT Services Brochure</div>
</section>

<!-- Page 7: Why choose -->
<section class="page" style="left:438px;top:1542px">
  <div class="photo" role="img" aria-label="Photo of a businessman in glasses typing on a laptop" style="left:0;top:0;width:344px;height:488px;background:linear-gradient(90deg,#ffffff 0%,#f6f8fa 45%,#c9d3dc 70%,#7f8f9e 88%,#5d6b79 100%)"></div>
  <div class="photo" role="img" aria-label="Laptop on the desk in the foreground" style="left:0;top:275px;width:150px;height:90px;background:linear-gradient(160deg,#d7dde2,#8d969e 60%,#3f4850)"></div>

  <h2 class="abs head" style="left:26px;top:34px;font-size:14px;line-height:1.4">WHY CHOOSE<br><span class="hl">QUARVELLA?</span></h2>

  <div class="why-sub" style="top:79px">EXPERTISE AND EXPERIENCE</div>
  <p class="why-text" style="top:92px">With years of experience in the IT industry, our team possesses the knowledge and skills to tackle any challenge. We stay abreast of the latest technological advancements to provide you with cutting-edge solutions.</p>
  <div class="why-sub" style="top:125px">CUSTOMER-CENTRIC APPROACH</div>
  <p class="why-text" style="top:138px">We prioritize our clients' needs and work closely with them to deliver customized solutions that drive success. Our client-centric approach ensures that we are always aligned with your business goals.</p>
  <div class="why-sub" style="top:171px">PROACTIVE SUPPORT</div>
  <p class="why-text" style="top:184px">Our proactive support model ensures that potential issues are identified and resolved before they can impact your operations. We are committed to maintaining the highest levels of service availability and performance.</p>
  <div class="why-sub" style="top:217px">COMPREHENSIVE SOLUTIONS</div>
  <p class="why-text" style="top:230px">From managed services to cybersecurity, we offer a comprehensive suite of IT solutions designed to meet the diverse needs of your business. Our holistic approach ensures that all aspects of your IT environment are covered.</p>

  <div class="foot-note" style="left:36px">Quarvella IT Services Brochure</div>
  <div class="rule" style="left:88px;width:205px;background:var(--pale)"><span class="run" style="left:145px;width:60px"></span></div>
  <div class="folio" style="left:303px;color:#fff">7</div>
</section>

<!-- Back cover -->
<section class="page" style="left:438px;top:2036px">
  <div class="photo" role="img" aria-label="Blue-tinted photo of a technician working on a server rack" style="left:0;top:0;width:344px;height:488px;background:linear-gradient(160deg,#1a8fe0 0%,#0677BA 35%,#0a4f8c 60%,#0b2f5a 85%,#081f3d 100%)"></div>
  <svg class="abs" width="344" height="488" viewBox="0 0 344 488" style="left:0;top:0">
    <circle cx="380" cy="150" r="150" fill="none" stroke="#0a4f9a" stroke-width="26" opacity=".85"/>
    <circle cx="380" cy="150" r="170" fill="none" stroke="#2da4ef" stroke-width="3"/>
  </svg>
  <div class="abs cover-brand" style="left:32px;top:94px;font-size:27px;color:#fff">Quarvella</div>
  <div class="abs cover-tag" style="left:118px;top:136px;font-size:7px;color:#fff">COMPUTING EXCELLENCE</div>

  <h2 class="abs head" style="left:57px;top:346px;font-size:16px;color:#fff">GET IN TOUCH</h2>
  <p class="abs" style="left:62px;top:369px;width:215px;font-size:4.5px;line-height:1.75;color:#d9eaf8">DISCOVER HOW QUARVELLA CAN TRANSFORM YOUR IT LANDSCAPE AND DRIVE YOUR BUSINESS FORWARD. CONTACT US TODAY TO LEARN MORE ABOUT OUR SERVICES AND HOW WE CAN HELP YOU ACHIEVE YOUR GOALS.</p>

  <div class="abs" style="left:56px;top:426px;width:78px;color:#fff">
    <div class="contact-head" style="color:#fff">Contact Us</div>
    <div class="tiny">Website: www.quarvella.co.uk<br>Email: info@quarvella.co.uk<br>Phone: 0161 555 0192</div>
  </div>
  <div class="abs" style="left:139px;top:427px;width:55px;color:#fff">
    <div class="contact-head caps" style="color:#fff">ADDRESS TO</div>
    <div class="tiny">48 Harbour Lane, Tech<br>Park, Leeds, UK</div>
  </div>
  <div class="abs" style="left:198px;top:426px;width:62px;color:#fff">
    <div class="contact-head" style="color:#fff">Follow Us</div>
    <div class="tiny">Stay updated with the latest<br>news and updates from Quarvella.</div>
  </div>
  <div class="abs tiny" style="left:265px;top:434px;color:#fff">Profile (QRV)<br>Feed (QRV)<br>Page (QRV)</div>
</section>

</main>
</body>
</html>
```